Lodging Venture Advisors

I am an independent operator engaged on short/medium term consultancy briefs within the Hotel/Resort sector in the Pacific Area and have a representation in Fiji.

A broad based services is offered and includes:

Development Advisory
Property Management
Sales & Marketing
Holiday Ownership/Timeshare
Resorts/Apartments/Motels/Flashpackers/B&B
Financial & Legal Referrals

Industry/Entity Type

Hotel

Contact Information for Business Card

Business name - LODGING VENTURE ADVISORS
My name - Grant Whitlock
Address: PO Box 382 Coral Heights 4219 Qld
Phone: Australia: +61 7 55904283 Mobile: 0418952064 (ChatLine)
Fiji: +679 8527319
Email: grantmwhitlock@netmailbox.example

```html
<!DOCTYPE html>
<html lang="en">
<head>
<meta charset="utf-8">
<title>Lodging Venture Advisors – Business Card</title>
<link rel="stylesheet" href="https://fonts.googleapis.com/css2?family=Cinzel:wght@400&family=Josefin+Sans:wght@300&display=swap">
<style>
  :root {
    --backdrop: #2b6a92;
    --card: #1b1a1a;
    --card-edge: #0e0e0e;
    --silver: #d2d2d2;
    --silver-soft: #b8b8b8;
  }
  * { box-sizing: border-box; margin: 0; padding: 0; }
  html, body { width: 1200px; height: 911px; overflow: hidden; }
  body {
    background: var(--backdrop);
    display: flex;
    align-items: center;
    justify-content: center;
    gap: 60px;
  }
  .card {
    position: relative;
    width: 520px;
    height: 318px;
    background: var(--card);
    border: 1px solid var(--card-edge);
    border-radius: 4px;
    color: var(--silver);
    box-shadow: 0 12px 30px rgba(0,0,0,0.35);
  }
  .brand-name {
    position: absolute;
    top: 34px;
    right: 34px;
    font-family: "Cinzel", serif;
    font-weight: 400;
    font-size: 25px;
    line-height: 1.05;
    letter-spacing: 2px;
    text-align: right;
    color: var(--silver);
  }
  .holder {
    position: absolute;
    left: 40px;
    top: 158px;
    font-family: "Josefin Sans", sans-serif;
    font-weight: 300;
    color: var(--silver-soft);
  }
  .holder-name {
    font-size: 17px;
    letter-spacing: 2px;
    margin-bottom: 10px;
    color: var(--silver);
  }
  .contact-line {
    font-size: 12.5px;
    letter-spacing: 1px;
    line-height: 1.45;
  }
  .services {
    position: absolute;
    left: 0;
    right: 0;
    top: 150px;
    list-style: none;
    text-align: center;
    font-family: "Josefin Sans", sans-serif;
    font-weight: 300;
    font-size: 14px;
    letter-spacing: 2px;
    line-height: 1.35;
    color: var(--silver-soft);
  }
</style>
</head>
<body>
  <section class="card card-front" aria-label="Business card front">
    <div class="brand-name">Lodging<br>Venture<br>Advisors</div>
    <div class="holder">
      <p class="holder-name">Grant Whitlock</p>
      <p class="contact-line">PO Box 382 Coral Heights 4219 Qld</p>
      <p class="contact-line">Australia: +61 7 55904283</p>
      <p class="contact-line">Mobile: 0418952064 (ChatLine)</p>
      <p class="contact-line">Fiji: +679 8527319</p>
      <p class="contact-line">grantmwhitlock@netmailbox.example</p>
    </div>
  </section>

  <section class="card card-back" aria-label="Business card back">
    <div class="brand-name">Lodging<br>Venture<br>Advisors</div>
    <ul class="services">
      <li>Development Advisory</li>
      <li>Property Management</li>
      <li>Sales &amp; Marketing</li>
      <li>Holiday Ownership/Timeshare</li>
      <li>Resorts/Apartments/Motels/Flashpackers/B&amp;B</li>
      <li>Financial &amp; Legal Referrals</li>
    </ul>
  </section>
</body>
</html>
```